Brenley Mechanical Drain Cleaning and Jetting

We need to show our customers and potential customers that we now have the ability to perform Drain Cleaning, camera inspections, location services, and Hydro-Jetting Services. I would like the the colors to match the previous design.

```html
<!DOCTYPE html>
<html lang="en">
<head>
<meta charset="utf-8">
<title>Brenley Mechanical – Drain Cleaning and Jetting</title>
<link rel="stylesheet" href="https://fonts.googleapis.com/css2?family=Oswald:wght@600;700&family=Open+Sans:ital,wght@0,400;0,700;1,400&display=swap">
<style>
  :root {
    --page-bg: #e6e6e6;
    --paper: #ffffff;
    --brand-green: #1d7a4f;
    --brand-green-deep: #145c3b;
    --tunnel-teal: #1f5f5a;
    --tunnel-dark: #0f3b3a;
    --tunnel-gold: #8f8a3a;
    --text-light: #ffffff;
    --icon-orange: #e8912d;
    --logo-green: #1a5e38;
  }
  * { margin: 0; padding: 0; box-sizing: border-box; }
  html, body { width: 1200px; height: 1200px; overflow: hidden; background: var(--page-bg); }
  .poster {
    position: absolute; left: 204px; top: 40px;
    width: 792px; height: 1120px; overflow: hidden;
    background: var(--brand-green);
    font-family: "Open Sans", Arial, sans-serif;
    color: var(--text-light);
  }
  .poster__top-band { position: absolute; left: 0; top: 0; width: 100%; height: 217px; background: var(--paper); }
  .poster__tunnel-photo {
    position: absolute; left: 0; top: 520px; width: 100%; height: 600px;
    background:
      radial-gradient(ellipse 28% 20% at 50% 22%, rgba(170,180,90,0.55), transparent 70%),
      radial-gradient(ellipse 70% 30% at 50% 88%, rgba(190,170,70,0.55), transparent 70%),
      linear-gradient(180deg, var(--brand-green) 0%, var(--tunnel-teal) 30%, var(--tunnel-dark) 65%, var(--tunnel-gold) 85%, var(--tunnel-dark) 100%);
  }
  .poster__shapes { position: absolute; left: 0; top: 0; }
  .brand {
    position: absolute; left: 261px; top: 62px; width: 270px;
    text-align: center; font-family: "Oswald", Arial, sans-serif; font-weight: 700;
    color: var(--logo-green); font-size: 34px; line-height: 38px; letter-spacing: 0.5px;
    text-transform: uppercase;
  }
  .headline {
    position: absolute; left: 0; top: 352px; width: 100%;
    text-align: center; font-family: "Oswald", Arial, sans-serif; font-weight: 600;
    font-size: 52px; line-height: 62px; letter-spacing: 0.5px; text-transform: uppercase;
  }
  .tagline {
    position: absolute; left: 0; top: 746px; width: 100%; text-align: center;
    font-style: italic; font-size: 14.5px; letter-spacing: 0.2px; text-transform: uppercase;
  }
  .toll-free {
    position: absolute; left: 0; top: 796px; width: 100%; text-align: center;
    font-weight: 700; font-size: 22px;
  }
  .contact-line {
    position: absolute; left: 0; top: 828px; width: 100%;
    display: flex; justify-content: center; align-items: center; gap: 10px;
    font-size: 21px;
  }
  .contact-line__item { display: flex; align-items: center; gap: 8px; }
  .contact-line__item + .contact-line__item { margin-left: 12px; }
  .contact-line svg { width: 22px; height: 22px; }
</style>
</head>
<body>
  <main class="poster">
    <div class="poster__top-band"></div>
    <div class="poster__tunnel-photo" role="img" aria-label="Photo looking down a round drainage tunnel with water reflecting light"></div>

    <svg class="poster__shapes" width="792" height="1120" viewBox="0 0 792 1120">
      <defs>
        <radialGradient id="pipe-camera-tone" cx="0.55" cy="0.45" r="0.6">
          <stop offset="0" stop-color="#121616"/>
          <stop offset="0.55" stop-color="#2c2a24"/>
          <stop offset="1" stop-color="#6b604c"/>
        </radialGradient>
        <radialGradient id="locator-map-tone" cx="0.4" cy="0.55" r="0.7">
          <stop offset="0" stop-color="#2f8fd6"/>
          <stop offset="0.5" stop-color="#0f3c78"/>
          <stop offset="1" stop-color="#061634"/>
        </radialGradient>
      </defs>
      <circle cx="38" cy="194" r="226" fill="var(--paper)"/>
      <circle cx="38" cy="194" r="218" fill="url(#pipe-camera-tone)" role="img" aria-label="Photo of an inspection camera inside a sewer pipe"/>
      <circle cx="754" cy="194" r="226" fill="var(--paper)"/>
      <circle cx="754" cy="194" r="218" fill="url(#locator-map-tone)" role="img" aria-label="Illustration of a glowing digital map route with location pins"/>
    </svg>

    <div class="brand">Brenley<br>Mechanical</div>

    <h1 class="headline">Drain Cleaning,<br>Camera Inspections,<br>Location Services, and<br>Hydro-Jetting Services</h1>

    <p class="tagline">New installations, service, and maintenance of all brands of equipment</p>

    <p class="toll-free">TOLL FREE: 1-800.GO.BRENLEY</p>

    <p class="contact-line">
      <span class="contact-line__item">
        <svg viewBox="0 0 24 24" aria-hidden="true"><path fill="var(--icon-orange)" d="M6.6 10.8a15.1 15.1 0 0 0 6.6 6.6l2.2-2.2a1 1 0 0 1 1-.25 11.4 11.4 0 0 0 3.6.57 1 1 0 0 1 1 1V20a1 1 0 0 1-1 1A17 17 0 0 1 3 4a1 1 0 0 1 1-1h3.5a1 1 0 0 1 1 1c0 1.25.2 2.45.57 3.57a1 1 0 0 1-.25 1z"/></svg>
        555-014-2870
      </span>
      <span class="contact-line__item">
        <svg viewBox="0 0 24 24" aria-hidden="true"><g fill="none" stroke="var(--icon-orange)" stroke-width="2"><circle cx="12" cy="12" r="9"/><ellipse cx="12" cy="12" rx="4" ry="9"/><path d="M3 12h18M5 7h14M5 17h14"/></g></svg>
        www.brenleymechanical.com
      </span>
    </p>
  </main>
</body>
</html>
```